Einladung zum Geburtstag
Einladung zu einer Geburtstagsparty von zwei "Mädels", die zusammen 99 Jahre jung werden.
Eine wird 55 (25.8.) die andere 44. (24.8.) - alles "Schnapszahlen".
Es soll eine kleine Party tagsüber für die Arbeitskollegen werden, mit Imbiss und Umtrunk. Termin für die Feier ist der 25.8. ab 14h.
Die Einladung soll sowohl gedruckt als auch per Mail verschickt werden können.

```html
<!DOCTYPE html>
<html lang="de">
<head>
<meta charset="utf-8">
<title>Einladung – 99 Jahre</title>
<link rel="stylesheet" href="https://fonts.googleapis.com/css2?family=Great+Vibes&display=swap">
<style>
  :root {
    --paper: #ffffff;
    --mist: #e6e8ec;
    --mist-soft: rgba(230, 232, 236, 0.85);
    --sand: #e3c994;
    --sand-column: rgba(214, 176, 104, 0.62);
    --ink: #141210;
    --ink-soft: #3a3530;
    --gift-gold: #d9b04a;
    --gift-cream: #f3e6c4;
    --gift-wine: #6e1f22;
  }
  html, body {
    margin: 0;
    padding: 0;
    overflow: hidden;
    background: var(--paper);
  }
  .invitation {
    position: relative;
    width: 1200px;
    height: 830px;
    overflow: hidden;
    background: var(--paper);
    font-family: Arial, Helvetica, sans-serif;
  }
  .band { position: absolute; left: 0; width: 1200px; }
  .band--top { top: 0; height: 87px; background: var(--mist); }
  .band--title { top: 110px; height: 128px; background: var(--sand); }
  .gift-photo {
    position: absolute;
    left: 0; top: 271px;
    width: 829px; height: 534px;
    background:
      radial-gradient(ellipse at 30% 55%, var(--gift-gold) 0%, rgba(217,176,74,0) 45%),
      radial-gradient(ellipse at 75% 75%, var(--gift-cream) 0%, rgba(243,230,196,0) 40%),
      radial-gradient(ellipse at 60% 40%, var(--gift-wine) 0%, rgba(110,31,34,0) 35%),
      linear-gradient(180deg, #f4ede0 0%, #e2c27a 45%, #b88a32 100%);
  }
  .band--age { top: 255px; height: 157px; background: var(--mist-soft); }
  .column {
    position: absolute;
    left: 905px; top: 0;
    width: 236px; height: 830px;
    background: var(--sand-column);
  }
  .script {
    position: absolute;
    margin: 0;
    font-family: "Great Vibes", cursive;
    font-weight: 400;
    line-height: 1;
    white-space: nowrap;
  }
  .title { left: 28px; top: 40px; font-size: 205px; color: var(--ink); }
  .age { left: 238px; top: 282px; font-size: 106px; color: var(--ink); }
  .date { left: 878px; top: 28px; font-size: 60px; color: var(--ink-soft); }
  .time { left: 910px; top: 112px; font-size: 80px; color: var(--ink-soft); }
  .message {
    position: absolute;
    left: 870px; top: 288px;
    width: 310px;
    margin: 0;
    text-align: center;
    font-size: 29px;
    line-height: 34.5px;
    color: var(--ink);
  }
</style>
</head>
<body>
  <main class="invitation">
    <div class="band band--top"></div>
    <div class="band band--title"></div>
    <div class="gift-photo" role="img" aria-label="Foto: gestapelte Geschenke in Gold, Creme und Weinrot mit goldenen Schleifen"></div>
    <div class="band band--age"></div>
    <div class="column"></div>

    <h1 class="script title">Einladung</h1>
    <p class="script age">99 Jahre</p>
    <p class="script date">25.08.2011</p>
    <p class="script time">14 Uhr</p>

    <p class="message">
      Wir wollen feiern,<br>
      den wir haben<br>
      zusammen fast<br>
      ein ganzen<br>
      Jahrhundert<br>
      geschafft.<br>
      Wir freuen uns<br>
      über jeden der mit<br>
      uns feiern<br>
      möchte..
    </p>
  </main>
</body>
</html>
```